We are looking for a poster / flyer to advertise our Squash Tournament - the Wrenfold Club Sydney CBD Squash Open. I have provided the details and sponsor logos that need to appear on the poster in the attachments.
I am open to the poster including pictures of real life squash playing action shots or a complete graphic art design.

Target Market(s)

Squash Players and Sporty People who may be interested in trying Squash as a new Sport

Requirements
Must have
• 1. All logos attached in files (logos in the word doc and the Bramwick Logo)
2. Content that has been provided in the word doc
3. Printable on A3 paper
4. Title of the poster must be 2021 Wrenfold Club Sydney CBD Squash Open
Nice to have
• 1.Design must be related to the Sport of Squash (can either be a graphic Design that incorporates a real life squash pic rom the internet or 100% graphic)
2. Something incorporating both female and junior squash player participation.
3. Poster depicts action / athleticism.

```html
<!DOCTYPE html>
<html lang="en">
<head>
<meta charset="utf-8">
<title>2021 Wrenfold Club Sydney CBD Squash Open</title>
<link rel="stylesheet" href="https://fonts.googleapis.com/css2?family=Montserrat:wght@700;800&family=Varela+Round&display=swap">
<style>
  :root {
    --navy: #0f2c6e;
    --blue: #2450b4;
    --deep-green: #1d4a26;
    --green: #2b5e2e;
    --yellow: #f6d40c;
    --gold: #e6b70f;
    --white: #ffffff;
    --ink: #16244a;
  }
  * { margin: 0; padding: 0; box-sizing: border-box; }
  html, body { width: 862px; height: 1200px; overflow: hidden; background: #f2f2f2; }
  .poster {
    position: relative; width: 862px; height: 1200px; overflow: hidden;
    font-family: "Varela Round", sans-serif; color: var(--ink);
  }
  .action-photo {
    position: absolute; inset: 0;
    background:
      radial-gradient(ellipse 60% 55% at 38% 55%, #f4f1ec 0%, #e9e4dc 45%, rgba(233,228,220,0) 75%),
      linear-gradient(90deg, #3a6fc0 0%, #c9d4e3 12%, #efece7 35%, #eef0f4 62%, #b8c8e6 84%, #2c5ab8 100%);
  }
  .edge-vignette {
    position: absolute; inset: 0;
    background:
      linear-gradient(180deg, rgba(37,82,176,0.85) 0%, rgba(37,82,176,0) 9%),
      linear-gradient(0deg, rgba(37,82,176,0.9) 0%, rgba(37,82,176,0.25) 12%, rgba(37,82,176,0) 24%);
  }
  .halo { position: absolute; left: 0; top: 0; width: 862px; height: 700px; }
  .title-block {
    position: absolute; right: 40px; top: 170px; width: 330px; text-align: right;
    transform: rotate(-6deg); transform-origin: right top; color: var(--white);
  }
  .title-year { font-family: "Montserrat", sans-serif; font-weight: 800; font-size: 112px; line-height: 1; letter-spacing: 1px; }
  .title-venue { font-family: "Montserrat", sans-serif; font-weight: 700; font-size: 37px; line-height: 1.05; margin-top: 8px; }
  .title-event {
    font-family: "Montserrat", sans-serif; font-weight: 800; font-size: 30px; line-height: 1;
    color: var(--yellow); text-align: center; width: 150px; margin: 14px 70px 0 auto;
  }
  .prize-badge {
    position: absolute; left: 112px; top: 246px; width: 236px; height: 236px; border-radius: 50%;
    background: var(--yellow); color: var(--deep-green);
    display: flex; flex-direction: column; justify-content: center; align-items: center;
    font-family: "Montserrat", sans-serif; font-weight: 800; transform: rotate(-28deg);
  }
  .prize-amount { font-size: 64px; line-height: 1; }
  .prize-label { font-size: 32px; line-height: 1; margin-top: 4px; }
  .event-details {
    position: absolute; right: 70px; top: 568px; text-align: right;
    font-family: "Montserrat", sans-serif; font-weight: 700; line-height: 1.1;
  }
  .event-dates { font-size: 30px; color: var(--green); }
  .event-courts { font-size: 30px; color: var(--navy); }
  .venue-list { position: absolute; right: 70px; top: 696px; text-align: right; font-family: "Montserrat", sans-serif; font-weight: 700; font-size: 21px; line-height: 1.5; color: var(--navy); }
  .grades-heading {
    position: absolute; left: 440px; top: 792px; width: 310px; height: 30px; padding-left: 20px;
    background: linear-gradient(90deg, rgba(230,183,15,0) 0%, var(--gold) 10%, var(--gold) 70%, rgba(230,183,15,0) 100%);
    font-family: "Montserrat", sans-serif; font-weight: 700; font-size: 21px; line-height: 30px; color: var(--deep-green);
  }
  .grades-list { position: absolute; left: 468px; top: 826px; list-style: none; font-size: 20px; line-height: 1.42; color: var(--navy); }
  .bar-band {
    position: absolute; left: 80px; top: 983px; width: 700px; height: 34px; border-radius: 17px;
    background: linear-gradient(90deg, rgba(36,80,180,0) 0%, var(--blue) 15%, var(--blue) 85%, rgba(36,80,180,0) 100%);
    color: var(--white); text-align: center; font-size: 19px; line-height: 34px;
  }
  .entry-note { position: absolute; left: 60px; width: 742px; top: 1024px; text-align: center; font-size: 17px; line-height: 1.35; color: var(--ink); }
  .entry-note strong { font-family: "Montserrat", sans-serif; font-weight: 700; color: var(--navy); }
  .sponsor-row {
    position: absolute; left: 40px; right: 30px; top: 1088px; height: 46px;
    display: flex; align-items: center; justify-content: space-between;
    font-family: "Montserrat", sans-serif; font-weight: 700; color: var(--navy);
  }
  .sponsor { display: flex; align-items: center; gap: 6px; font-size: 15px; white-space: nowrap; }
  .sponsor-mark { width: 30px; height: 30px; border-radius: 50%; background: var(--gold); }
  .sponsor-badge { width: 64px; height: 44px; border-radius: 10px; background: var(--navy); }
  .sponsor-badge.round { width: 44px; border-radius: 50%; background: #1c3172; }
  .sponsor.large { font-size: 26px; letter-spacing: 1px; color: #1a1a1a; }
  .director { position: absolute; left: 0; right: 0; top: 1160px; text-align: center; font-size: 14px; color: #1a1a1a; word-spacing: 2px; }
  .director strong { font-family: "Montserrat", sans-serif; font-weight: 700; }
</style>
</head>
<body>
<main class="poster">
  <div class="action-photo" role="img" aria-label="Action photo of a male squash player holding a blue racquet in the foreground and a female player ready on a white squash court"></div>
  <div class="edge-vignette"></div>

  <svg class="halo" viewBox="0 0 862 700" aria-hidden="true">
    <g fill="#1d4a26">
      <circle cx="470" cy="110" r="200" opacity="0.12"/>
      <circle cx="515" cy="150" r="205" opacity="0.14"/>
      <circle cx="560" cy="190" r="208" opacity="0.18"/>
      <circle cx="605" cy="230" r="210" opacity="0.22"/>
      <circle cx="650" cy="265" r="212" opacity="0.3"/>
      <circle cx="690" cy="300" r="215" opacity="0.92"/>
    </g>
  </svg>

  <div class="title-block">
    <div class="title-year">2021</div>
    <div class="title-venue">WRENFOLD<br>CLUB, SYDNEY</div>
    <div class="title-event">CBD<br>SQUASH<br>OPEN</div>
  </div>

  <div class="prize-badge">
    <span class="prize-amount">$14k</span>
    <span class="prize-label">in prize<br>money</span>
  </div>

  <div class="event-details">
    <div class="event-dates">13-15<br>August 2021</div>
    <div class="event-courts">CBD Courts</div>
  </div>

  <div class="venue-list">
    (Wrenfold &amp; Harrowgate Clubs)<br>
    &amp; Kestrel Uni. Sports &amp; Fitness<br>
    All finals at Wrenfold Club
  </div>

  <div class="grades-heading">Grades available</div>
  <ol class="grades-list">
    <li>1. Mens and Ladies Squash Open,</li>
    <li>2. Racquetball Open</li>
    <li>3. Junior events</li>
    <li>4. All grades / abilities catered for</li>
  </ol>

  <div class="bar-band">Saturday Night Open Bar in CBD provided by Sponsor ($3K bar tab)</div>
  <p class="entry-note">Players guaranteed 3 matches $60 entry fee. Weekday matches also organised for CBD workers preferring to play during the day. <strong>Entries close 7th August 2021</strong></p>

  <div class="sponsor-row">
    <span class="sponsor"><span class="sponsor-mark"></span>Kestrel Uni</span>
    <span class="sponsor">WRENFOLD CLUB</span>
    <span class="sponsor-badge"></span>
    <span class="sponsor">harrowgate</span>
    <span class="sponsor-badge round"></span>
    <span class="sponsor large">BRAMWICK</span>
  </div>

  <p class="director"><strong>Tournament Director:</strong> Daniel Ashford &nbsp; Daniel.Ashford@mailpost.net &nbsp; 0491570182</p>
</main>
</body>
</html>
```